Doctors clinic requires stationary designed

We require various types of stationary to be design based on the logo (attached). We require the following:
- Letterhead (A4 Portrait)
- Business Card (must include UV spot on rear)
- With compliments slip (DL Landscape)
- Appointments card (Folded A6)

We are a young clinical practice which boasts a modern and sophisticated approach to medicine so we require something which feels fresh and modern. Please include colours represented in the logo (contrasting teal and grey). We are calling for creative minds to put forth their ideas and we will be actively providing feedback on all designs.

thank you

Clinic

```html
<!DOCTYPE html>
<html lang="en">
<head>
<meta charset="utf-8">
<title>Dr Helena Marsh – Stationery Set</title>
<link href="https://fonts.googleapis.com/css2?family=Open+Sans:wght@400;600;700&family=Italianno&display=swap" rel="stylesheet">
<style>
  :root {
    --backdrop: #e8e5e0;
    --paper: #ffffff;
    --teal: #1d9488;
    --teal-soft: #6cc2b4;
    --ink: #4a4a4a;
    --ink-light: #8a8a8a;
    --metal-dark: #1f1f1f;
    --metal-mid: #3c3c3c;
    --on-dark: #e6e6e6;
    --faint: #dcecea;
  }
  * { box-sizing: border-box; margin: 0; padding: 0; }
  html, body { width: 1200px; height: 838px; overflow: hidden; }
  body {
    position: relative;
    background: var(--backdrop);
    font-family: "Open Sans", Arial, sans-serif;
    color: var(--ink);
  }
  .sheet { position: absolute; background: var(--paper); box-shadow: 0 1px 4px rgba(0,0,0,.25); overflow: hidden; }
  .sheet--dark { background: linear-gradient(180deg, var(--metal-mid) 0%, var(--metal-dark) 55%, #2a2a2a 100%); color: var(--on-dark); }

  .brand { position: absolute; display: flex; align-items: center; }
  .brand__mark { border: 2px solid var(--teal); border-radius: 50%; flex: none; }
  .brand__text { margin-left: 10px; }
  .brand__name { color: var(--teal); font-weight: 600; letter-spacing: -0.3px; line-height: 1.05; white-space: nowrap; }
  .brand__role { color: var(--teal); font-weight: 600; line-height: 1.2; white-space: nowrap; }

  .contacts { position: absolute; list-style: none; }
  .contacts li { display: flex; align-items: center; white-space: nowrap; }
  .contacts svg { flex: none; fill: none; stroke: var(--teal-soft); stroke-width: 1.4; }

  .address { position: absolute; text-align: right; white-space: nowrap; }
  .tab { position: absolute; background: var(--teal); border-radius: 3px; }

  .script-title { position: absolute; font-family: "Italianno", cursive; color: #555; font-size: 56px; line-height: 1; }

  .holder { position: absolute; text-align: right; }
  .holder__name { color: var(--teal); font-weight: 600; font-size: 9px; }
  .holder__title { color: var(--teal-soft); font-size: 6px; }
  .sheet--dark .holder__name { color: var(--on-dark); }

  .caption { position: absolute; font-size: 8px; color: #555; transform: translateX(-50%); letter-spacing: .3px; }

  .back-mark { position: absolute; left: 86px; top: 22px; width: 92px; height: 92px; border: 2px solid #f2f2f2; border-radius: 50%; display: flex; align-items: center; justify-content: center; text-align: center; color: #f2f2f2; font-weight: 600; font-size: 12px; line-height: 1.2; }
  .back-url { position: absolute; left: 0; right: 0; top: 128px; text-align: center; font-size: 8px; letter-spacing: 2.2px; color: #f2f2f2; }
  .watermark { position: absolute; border: 2px solid var(--faint); border-radius: 50%; }
</style>
</head>
<body>

<svg width="0" height="0" style="position:absolute" aria-hidden="true">
  <symbol id="icon-phone" viewBox="0 0 10 10"><circle cx="5" cy="5" r="4.3"/><path d="M3.4 3 q0 3.5 3.6 4 l.5-1-1-.6-.5.5q-1-.5-1.4-1.5l.5-.5-.6-1z"/></symbol>
  <symbol id="icon-fax" viewBox="0 0 10 10"><rect x="1.5" y="4" width="7" height="4" rx=".6"/><path d="M3 4V2h4v2M3 6.2h4"/></symbol>
  <symbol id="icon-mail" viewBox="0 0 10 10"><rect x="1.2" y="2.5" width="7.6" height="5.2" rx=".5"/><path d="M1.4 2.8 5 5.6l3.6-2.8"/></symbol>
  <symbol id="icon-web" viewBox="0 0 10 10"><circle cx="5" cy="5" r="4"/><path d="M1 5h8M5 1q-2.3 4 0 8M5 1q2.3 4 0 8"/></symbol>
</svg>

<!-- With compliments slip -->
<section class="sheet compliments" style="left:27px;top:194px;width:549px;height:259px;">
  <div class="brand" style="left:13px;top:17px;">
    <div class="brand__mark" style="width:60px;height:60px;"></div>
    <div class="brand__text">
      <div class="brand__name" style="font-size:20px;">Dr Helena Marsh</div>
      <div class="brand__role" style="font-size:11px;">Obstetrician and Gynaecologist</div>
    </div>
  </div>
  <div class="script-title" style="left:285px;top:34px;">With Compliments</div>
  <div class="tab" style="left:0;top:186px;width:6px;height:64px;"></div>
  <ul class="contacts" style="left:11px;top:188px;font-size:10px;line-height:14.6px;">
    <li><svg width="10" height="10"><use href="#icon-phone"/></svg>&nbsp;9123 4567</li>
    <li><svg width="10" height="10"><use href="#icon-fax"/></svg>&nbsp;9123 4567</li>
    <li><svg width="10" height="10"><use href="#icon-mail"/></svg>&nbsp;your.names@drhelenamarsh.com.au</li>
    <li><svg width="10" height="10"><use href="#icon-web"/></svg>&nbsp;www.drhelenamarsh.com.au</li>
  </ul>
  <div class="address" style="right:12px;top:218px;font-size:10px;line-height:14px;">Suite 4 Coastal Med. Centre (North)Harbour Ave<br>Millbrook, Zip Code - 000000</div>
  <div class="tab" style="right:0;top:219px;width:6px;height:27px;"></div>
</section>

<!-- Business card front, light -->
<section class="sheet card card--light" style="left:38px;top:481px;width:264px;height:150px;">
  <div class="brand" style="left:10px;top:11px;">
    <div class="brand__mark" style="width:44px;height:44px;"></div>
    <div class="brand__text" style="margin-left:8px;">
      <div class="brand__name" style="font-size:13px;">Dr Helena Marsh</div>
      <div class="brand__role" style="font-size:8px;">Obstetrician and Gynaecologist</div>
    </div>
  </div>
  <div class="tab" style="left:0;top:71px;width:4px;height:66px;"></div>
  <ul class="contacts" style="left:10px;top:72px;font-size:7px;line-height:10.5px;">
    <li><svg width="7" height="7"><use href="#icon-phone"/></svg>&nbsp;9123 4567</li>
    <li><svg width="7" height="7"><use href="#icon-fax"/></svg>&nbsp;9123 4567</li>
    <li><svg width="7" height="7"><use href="#icon-mail"/></svg>&nbsp;your.names@drhelenamarsh.com.au</li>
    <li><svg width="7" height="7"><use href="#icon-web"/></svg>&nbsp;www.drhelenamarsh.com.au</li>
    <li>Suite 4 Coastal Med. Centre (North)Harbour Ave</li>
    <li>Millbrook, Zip Code - 000000</li>
  </ul>
  <div class="holder" style="right:9px;top:95px;"><div class="holder__name">Your Name</div><div class="holder__title">Title</div></div>
  <div class="tab" style="right:0;top:95px;width:4px;height:20px;"></div>
</section>
<div class="caption" style="left:165px;top:638px;">BC_FRONT_1</div>

<!-- Business card front, dark -->
<section class="sheet sheet--dark card card--dark" style="left:317px;top:481px;width:264px;height:150px;">
  <div class="brand" style="left:10px;top:11px;">
    <div class="brand__mark" style="width:44px;height:44px;"></div>
    <div class="brand__text" style="margin-left:8px;">
      <div class="brand__name" style="font-size:13px;">Dr Helena Marsh</div>
      <div class="brand__role" style="font-size:8px;">Obstetrician and Gynaecologist</div>
    </div>
  </div>
  <div class="tab" style="left:0;top:71px;width:4px;height:66px;"></div>
  <ul class="contacts" style="left:10px;top:72px;font-size:7px;line-height:10.5px;">
    <li><svg width="7" height="7"><use href="#icon-phone"/></svg>&nbsp;9123 4567</li>
    <li><svg width="7" height="7"><use href="#icon-fax"/></svg>&nbsp;9123 4567</li>
    <li><svg width="7" height="7"><use href="#icon-mail"/></svg>&nbsp;your.names@drhelenamarsh.com.au</li>
    <li><svg width="7" height="7"><use href="#icon-web"/></svg>&nbsp;www.drhelenamarsh.com.au</li>
    <li>Suite 4 Coastal Med. Centre (North)Harbour Ave</li>
    <li>Millbrook, Zip Code - 000000</li>
  </ul>
  <div class="holder" style="right:9px;top:95px;"><div class="holder__name">Your Name</div><div class="holder__title">Title</div></div>
  <div class="tab" style="right:0;top:95px;width:4px;height:20px;"></div>
</section>
<div class="caption" style="left:445px;top:638px;">BC_FRONT_2</div>

<!-- Business card back -->
<section class="sheet sheet--dark card card--back" style="left:191px;top:654px;width:263px;height:149px;">
  <div class="back-mark">Dr Helena<br>Marsh</div>
  <div class="back-url">www.drhelenamarsh.com.au</div>
</section>
<div class="caption" style="left:322px;top:811px;">BC_BACK</div>

<!-- Letterhead -->
<section class="sheet letterhead" style="left:613px;top:33px;width:548px;height:776px;">
  <div class="brand" style="left:21px;top:12px;">
    <div class="brand__mark" style="width:59px;height:59px;"></div>
    <div class="brand__text">
      <div class="brand__name" style="font-size:19px;">Dr Helena Marsh</div>
      <div class="brand__role" style="font-size:10.5px;">Obstetrician and Gynaecologist</div>
    </div>
  </div>
  <div class="watermark" style="left:227px;top:700px;width:70px;height:70px;"></div>
  <div class="tab" style="left:0;top:704px;width:5px;height:63px;"></div>
  <ul class="contacts" style="left:10px;top:705px;font-size:10px;line-height:14.6px;">
    <li><svg width="10" height="10"><use href="#icon-phone"/></svg>&nbsp;9123 4567</li>
    <li><svg width="10" height="10"><use href="#icon-fax"/></svg>&nbsp;9123 4567</li>
    <li><svg width="10" height="10"><use href="#icon-mail"/></svg>&nbsp;your.names@drhelenamarsh.com.au</li>
    <li><svg width="10" height="10"><use href="#icon-web"/></svg>&nbsp;www.drhelenamarsh.com.au</li>
  </ul>
  <div class="address" style="right:12px;top:736px;font-size:10px;line-height:14px;">Suite 4 Coastal Med. Centre (North)Harbour Ave<br>Millbrook, Zip Code - 000000</div>
  <div class="tab" style="right:0;top:737px;width:6px;height:26px;"></div>
</section>

</body>
</html>
```